Zielgruppe
Es geht bei dem Projekt ( Briefpapier ) darum mein Buch zu promoten;:
Rechtsberatung für die Geschäftsführer von Etiketten- und Verpackungsdruckereien
Titel morgen leiser gehen ( Cover im Anhang )
Darüber hinaus soll eben auch meine geschäftliche Funktion erläutert werden
Aufgabenstellung
Es sollen mindestens alle Elemente des Briefpapierentwurfs ( Anhang ) enthalten sein. Gerne auch weitere Elemente meiner Vita ( Speaker etc. )

```html
<!DOCTYPE html>
<html lang="de">
<head>
<meta charset="utf-8">
<title>Briefpapier – Jonas Brettner</title>
<link rel="stylesheet" href="https://fonts.googleapis.com/css2?family=Open+Sans:wght@400;600&display=swap">
<style>
  :root {
    --backdrop: #55585c;
    --paper: #ffffff;
    --accent: #f5b400;
    --ink: #3a3a3a;
    --ink-soft: #8a8a8a;
    --rule: #c9c9c9;
    --band-top: #3b3c3f;
    --band-bottom: #232426;
    --signature: #2a3f8f;
  }
  * { box-sizing: border-box; margin: 0; padding: 0; }
  html, body { width: 1200px; height: 946px; overflow: hidden; }
  body {
    background: var(--backdrop);
    font-family: "Open Sans", Arial, sans-serif;
    color: var(--ink);
    position: relative;
  }
  .letterhead {
    position: absolute;
    left: 280px; top: 20px;
    width: 640px; height: 906px;
    background: var(--paper);
    overflow: hidden;
  }
  .brand {
    position: absolute; left: 70px; top: 40px;
    display: flex; gap: 10px; align-items: flex-start;
  }
  .brand-square { width: 20px; height: 20px; background: var(--accent); margin-top: 6px; }
  .brand-name {
    color: var(--accent); font-weight: 400; font-size: 24px; line-height: 24px;
  }
  .sender-line {
    position: absolute; left: 70px; top: 128px;
    font-size: 7.5px; color: var(--ink-soft); letter-spacing: .2px;
  }
  .contact-panel {
    position: absolute; left: 420px; top: 150px; width: 190px;
    border-left: 1px solid var(--rule); padding-left: 14px;
    font-size: 7.5px; line-height: 1.6; color: var(--ink-soft);
  }
  .contact-name {
    color: var(--accent); font-size: 15px; font-weight: 600;
    border-bottom: 1px solid var(--accent); padding-bottom: 3px; margin-bottom: 8px;
  }
  .contact-group { margin-bottom: 8px; }
  .contact-row { display: flex; align-items: center; gap: 5px; }
  .contact-row svg { width: 8px; height: 8px; fill: var(--accent); }
  .letter-body {
    position: absolute; left: 70px; top: 275px; width: 500px;
    font-size: 9.5px; line-height: 1.6; color: var(--ink);
  }
  .salutation { margin-bottom: 14px; }
  .letter-body p + p { margin-top: 10px; }
  .closing {
    position: absolute; left: 70px; top: 560px;
    font-size: 9px; color: var(--ink);
  }
  .signature {
    display: block; width: 150px; height: 38px; margin: 6px 0 4px;
    background: linear-gradient(90deg, rgba(42,63,143,.25), rgba(42,63,143,.08));
    border-radius: 4px;
  }
  .signer { font-size: 8px; color: var(--ink-soft); }
  .promo-band {
    position: absolute; left: 0; bottom: 0; width: 100%; height: 200px;
    background: linear-gradient(180deg, var(--band-top), var(--band-bottom));
    border-top: 3px solid var(--accent);
    border-bottom: 5px solid var(--accent);
  }
  .promo-claim {
    position: absolute; left: 70px; top: 48px;
    font-size: 18px; line-height: 1.35; color: #ffffff;
  }
  .promo-claim .topic { color: var(--accent); display: block; }
  .author-photo {
    position: absolute; right: 40px; bottom: 0; width: 170px; height: 160px;
    background: radial-gradient(ellipse at 55% 40%, #9a9590 0%, #4a4745 45%, #1f1f20 100%);
  }
</style>
</head>
<body>
  <main class="letterhead">
    <div class="brand">
      <span class="brand-square"></span>
      <div class="brand-name">morgen<br>leiser<br>gehen</div>
    </div>
    <div class="sender-line">Jonas Brettner · Lindenweg 14 · 40210 Düsseldorf</div>

    <aside class="contact-panel">
      <div class="contact-name">Jonas Brettner</div>
      <div class="contact-group">
        Rechtsanwalt &amp; Speaker<br>
        Autor des Buches „morgen leiser gehen“
      </div>
      <div class="contact-group">
        Lindenweg 14<br>
        40210 Düsseldorf
      </div>
      <div class="contact-row">
        <svg viewBox="0 0 10 10"><path d="M2 0h2l1 3-1.5 1a6 6 0 0 0 2.5 2.5L7 5l3 1v2c0 1-1 2-2 2A8 8 0 0 1 0 2c0-1 1-2 2-2z"/></svg>
        T +49 211 555 0142
      </div>
      <div class="contact-row">
        <svg viewBox="0 0 10 10"><path d="M0 2h10v6H0z M0 2l5 3.5L10 2" fill="none" stroke="#f5b400" stroke-width="1"/></svg>
        kontakt@brettner-recht.de
      </div>
    </aside>

    <section class="letter-body">
      <div class="salutation">Sehr geehrte Damen und Herren,</div>
      <p>in der Druckbranche entscheiden oft wenige Zeilen im Vertrag über Gewinn oder Verlust. Viele Geschäftsführer unterschreiben unter Zeitdruck und bemerken die Risiken erst, wenn es bereits zu spät ist. Genau hier setzt meine Beratung an.</p>
      <p>Als Rechtsanwalt begleite ich Etiketten- und Verpackungsdruckereien bei Einkauf, Lieferverträgen und Haftungsfragen. Mein Buch zeigt praxisnah, welche Klauseln Sie prüfen sollten, bevor Sie unterschreiben.</p>
      <p>Gerne stehe ich Ihnen für ein persönliches Gespräch oder einen Vortrag in Ihrem Unternehmen zur Verfügung. Ich freue mich auf Ihre Nachricht.</p>
    </section>

    <div class="closing">
      Mit freundlichen Grüßen
      <span class="signature" role="img" aria-label="Handschriftliche Unterschrift"></span>
      <div class="signer">Jonas Brettner</div>
    </div>

    <footer class="promo-band">
      <div class="promo-claim">
        <span class="topic">Druckindustrie:</span>
        Der beste Vertrag ist der schlechte,<br>
        den man nicht unterschreibt.
      </div>
      <div class="author-photo" role="img" aria-label="Porträtfoto des Autors im dunklen Anzug"></div>
    </footer>
  </main>
</body>
</html>
```